Family Medicine Clinic Needs Mailchimp Newsletter Template

Looking for a responsive mailchimp template that matches the theme and overall look/feel of our website brightpathhc.com.

I'm looking for a professional, clean, simple, minimalist, bold design.
Colors would ideally be greens and blues, cool tones, muted colors, or graytones.

See attached word document for content for the upcoming newsletter

Can see prior newsletter content here:
http://brightpathhc.com/ourresources/newsletter-archive/

I have attached a copy of our brochure to see a sample of what we offer

The desired newsletter title would be:
The Bright Path
Looking for a great banner for that

Looking for basically 1 main photo area per text area for future templates

Under September is Comfort Outreach Month want links to our different services I mention

Under the videos section would like a video gallery of sorts that have links to the videos

Lumaderm image ad needs to be redone

Would like a button to take to schedule an appointment and patient portal
Easily visible phone number
Would like to have several sections with buttons to find out more

Would like feedback question at bottom
Rated 7-10 would forward to
https://zipqa.lnk/Rb8kWe

1-6 would send email to us

Reason: I have now guaranteed payment so I am giving a few more days for those designers that still want to submit a design

```html
<!DOCTYPE html>
<html lang="en">
<head>
<meta charset="utf-8">
<title>The Bright Path – Newsletter Revisions</title>
<link href="https://fonts.googleapis.com/css2?family=Arimo:wght@400;700&family=Dosis:wght@500;600&family=Exo+2:ital,wght@1,800&display=swap" rel="stylesheet">
<style>
:root{
  --blue:#35a3d6;
  --blue-dark:#2a7fa3;
  --green:#9bc53d;
  --green-btn:#8cc63f;
  --indigo:#4e62b7;
  --navy:#1f4e6b;
  --ink:#111;
  --gray:#666;
  --light:#eef1f4;
  --white:#fff;
}
*{box-sizing:border-box;margin:0;padding:0}
html,body{width:1200px;height:3028px;overflow:hidden;background:var(--white);font-family:"Arimo",Arial,sans-serif;color:var(--ink)}
.board{position:relative;width:1200px;height:3028px}
.abs{position:absolute}
.sheet-title{left:456px;top:76px;font-weight:700;font-size:26px;letter-spacing:1px}
.note{left:40px;width:340px;font-weight:700;font-size:20px;line-height:24px}
/* header */
.masthead{left:456px;top:150px;width:712px;height:58px;background:var(--blue);color:var(--white);display:flex;align-items:center;justify-content:space-between;padding:0 30px 0 20px}
.masthead h1{font-size:30px;font-weight:700;letter-spacing:1px}
.masthead a{font-size:16px;color:var(--white);text-decoration:none}
.brandbar{left:456px;top:208px;width:712px;height:104px;background:var(--light);display:flex;align-items:center;justify-content:space-between;padding:0 34px 0 24px}
.brand{display:flex;align-items:center;gap:14px;font-size:34px;font-weight:700;color:var(--blue-dark)}
.brand i{width:30px;height:30px;border-radius:50%;background:var(--green)}
.phone{display:flex;align-items:center;gap:18px;font-size:28px;color:var(--blue-dark)}
.phone span.dot{width:56px;height:56px;border-radius:50%;background:var(--green);display:flex;align-items:center;justify-content:center}
/* hero */
.hero-photo{left:456px;top:312px;width:354px;height:358px;background:linear-gradient(135deg,#cfe6f2,#8fbcd6 60%,#d8c0a8)}
.hero-panel{left:810px;top:312px;width:358px;height:358px;background:var(--green);color:var(--white);text-align:center}
.hero-panel h2{font-family:"Dosis",sans-serif;font-weight:500;font-size:47px;line-height:48px;margin-top:40px;letter-spacing:1px}
.btn-outline{display:block;margin:40px auto 0;width:302px;height:56px;border:3px solid var(--white);color:var(--white);font-size:17px;font-weight:700;letter-spacing:1px;line-height:50px;text-decoration:none}
/* issue */
.issue{left:456px;top:670px;width:354px;height:330px;background:var(--blue);color:var(--white);padding:18px 20px}
.issue h3{font-size:21px;font-weight:700;margin-bottom:8px}
.issue li{list-style:none;font-size:15.5px;line-height:26px;padding-left:24px;position:relative}
.issue li::before{content:"";position:absolute;left:0;top:9px;width:10px;height:10px;border-radius:50%;background:var(--white)}
.issue li a{color:var(--white)}
.supplement{left:810px;top:670px;width:358px;height:330px;background:linear-gradient(160deg,#6e6e6e,#3f3f3f);color:var(--white);text-align:center}
.supplement p{font-size:20px;line-height:32px;margin-top:48px}
.supplier{display:flex;align-items:center;justify-content:center;gap:10px;margin-top:20px;font-size:36px;font-weight:700}
.supplier i{width:30px;height:30px;border-radius:50%;background:var(--green)}
.btn-pill{display:block;margin:34px auto 0;width:268px;height:56px;border-radius:28px;background:var(--green-btn);color:var(--white);font-size:26px;font-weight:700;line-height:56px;text-decoration:none;letter-spacing:1px}
.tab{top:1000px;height:62px;color:var(--white);font-size:21px;font-weight:700;text-align:center;line-height:62px}
.tab.social{left:456px;width:354px;background:var(--indigo)}
.tab.dates{left:810px;width:358px;background:var(--green-btn)}
.social-text{left:466px;top:1082px;width:300px;font-size:15.5px;line-height:24px;color:var(--gray)}
.like{left:468px;top:1146px;width:64px;height:24px;background:var(--indigo);color:var(--white);font-size:13px;font-weight:700;text-align:center;line-height:24px;border-radius:2px}
.dates-list{left:838px;top:1080px;width:320px;font-size:15px;line-height:28px;color:var(--gray);font-weight:700}
.dates-list b{color:var(--blue);font-weight:400;font-size:17px}
/* month banner */
.month{left:456px;top:1200px;width:714px;height:244px;border:6px solid #a9d7ef;background:linear-gradient(160deg,var(--blue-dark) 0 55%,#3a93b8 55% 75%,var(--blue-dark) 75%);overflow:hidden}
.month .band{position:absolute;left:0;top:62px;width:540px;height:120px;background:var(--blue)}
.month h2{position:absolute;left:22px;top:56px;font-family:"Exo 2",sans-serif;font-style:italic;font-weight:800;font-size:62px;color:var(--white);letter-spacing:3px}
.month p{position:absolute;left:30px;top:134px;font-family:"Exo 2",sans-serif;font-style:italic;font-weight:800;font-size:27px;color:var(--navy)}
.month .figure{position:absolute;right:0;top:0;width:250px;height:232px;background:linear-gradient(90deg,rgba(255,255,255,0),#cfcfcf 40%,#8a8a8a)}
/* services */
.intro{left:456px;top:1510px;width:712px;text-align:center;font-size:17px;font-weight:700;color:var(--gray);line-height:34px}
.service{width:200px;text-align:center;color:var(--blue);font-weight:700;font-size:17px;line-height:21px}
.service .ic{width:88px;height:88px;border-radius:50%;background:var(--green);margin:0 auto 14px;display:flex;align-items:center;justify-content:center}
/* testimonials */
.t-head{left:460px;top:2010px;width:712px;height:46px;background:var(--blue);color:var(--white);font-size:23px;font-weight:700;text-align:center;line-height:46px;letter-spacing:1px}
.video{background:var(--green-btn)}
.video .still{height:236px;background:linear-gradient(135deg,#c9c2b6,#8d8579);position:relative}
.video .still svg{position:absolute;left:50%;top:50%;transform:translate(-50%,-50%)}
.video .name{height:46px;color:var(--white);font-weight:700;font-size:18px;text-align:center;line-height:46px}
</style>
</head>
<body>
<div class="board">
  <div class="abs sheet-title">REVISIONS AS PER YOUR FEEDBACK-PART 1</div>

  <div class="abs note" style="top:164px">New header with title</div>
  <div class="abs note" style="top:244px">Logo small size, phone no introduced</div>
  <div class="abs note" style="top:430px">Banner and apppointment button. This whole part might use as a link for appointment</div>
  <div class="abs note" style="top:734px">in this issue part</div>
  <div class="abs note" style="top:1276px">You like this banner than others. Some colrs has changed to your theme</div>
  <div class="abs note" style="top:1732px">Icons create as per your advice.</div>
  <div class="abs note" style="top:2336px">Patient Testimonials - 5</div>

  <header class="abs masthead"><h1>THE BRIGHT PATH</h1><a href="#">view this email in your browser</a></header>
  <div class="abs brandbar">
    <div class="brand"><i></i>Bright Path</div>
    <div class="phone"><span class="dot"><svg width="28" height="28" viewBox="0 0 24 24"><path fill="#fff" d="M6.6 10.8a15 15 0 0 0 6.6 6.6l2.2-2.2c.3-.3.7-.4 1-.2 1.1.4 2.3.6 3.6.6.6 0 1 .4 1 1V20c0 .6-.4 1-1 1A17 17 0 0 1 3 4c0-.6.4-1 1-1h3.5c.6 0 1 .4 1 1 0 1.3.2 2.5.6 3.6.1.3 0 .7-.2 1z"/></svg></span>(555) 240-7781</div>
  </div>

  <div class="abs hero-photo" role="img" aria-label="Photo of a smiling family of four lying together"></div>
  <div class="abs hero-panel">
    <h2>HELPING YOU<br>TO GET WELL,<br>LIVE WELL,<br>AND STAY WELL</h2>
    <a class="btn-outline" href="#">SCHEDULE AN APPOINTMENT</a>
  </div>

  <section class="abs issue">
    <h3>IN THIS ISSUE:</h3>
    <ul>
      <li><a href="#">Comfort Outreach Month</a></li>
      <li><a href="#">15 minutes of fame</a></li>
      <li><a href="#">It's Official</a></li>
      <li><a href="#">Don't Operate, Regenerate!</a></li>
      <li><a href="#">Back to School Lumaderm Special</a></li>
      <li><a href="#">Your Sinus Solution</a></li>
      <li><a href="#">Breast Thermography</a></li>
      <li><a href="#">Get Fit for Fall</a></li>
      <li><a href="#">Recipe of the Month</a></li>
      <li><a href="#">Feedback Wanted</a></li>
    </ul>
  </section>
  <section class="abs supplement" role="img" aria-label="Dim shelf of supplement bottles behind the offer">
    <p>Purchase professional-grade<br>supplements through</p>
    <div class="supplier"><i></i>Nutrisource</div>
    <a class="btn-pill" href="#">PLACE ORDER</a>
  </section>

  <div class="abs tab social">Like Us In Friendloop</div>
  <div class="abs tab dates">Upcoming Dates</div>
  <p class="abs social-text">Please like and follow us on Friendloop! We share regular updates and health tips.</p>
  <div class="abs like">Like</div>
  <div class="abs dates-list"><b>9/18</b> -- Get Fit For Fall Kickoff<br><b>9/22-23rd</b> -- Back to School Lumaderm<br>Special</div>

  <div class="abs month">
    <div class="band"></div>
    <h2>SEPTEMBER</h2>
    <p>IS COMFORT OUTREACH MONTH</p>
    <div class="figure" role="img" aria-label="Photo of a man holding his lower back, pain area glowing red"></div>
  </div>

  <p class="abs intro">Check out some of the many services we have that can help you with<br>your pain:</p>

  <div class="abs service" style="left:476px;top:1612px"><div class="ic"><svg width="52" height="52" viewBox="0 0 52 52" fill="none" stroke="#fff" stroke-width="3"><circle cx="16" cy="18" r="5"/><path d="M6 30h40M10 30v12M42 30v12M22 24h18"/></svg></div>OSTEOPATHIC<br>MANIPULATION</div>
  <div class="abs service" style="left:700px;top:1612px"><div class="ic"><svg width="52" height="52" viewBox="0 0 52 52" fill="none" stroke="#fff" stroke-width="3"><circle cx="14" cy="22" r="5"/><path d="M6 32h40M12 32v10M40 32v10M22 28h18M30 8v14M36 10v12"/></svg></div>ACUPUNTURE</div>
  <div class="abs service" style="left:942px;top:1612px"><div class="ic"><svg width="52" height="52" viewBox="0 0 52 52" fill="none" stroke="#fff" stroke-width="3"><path d="M14 38l20-20M30 14l8 8M36 10l6 6M14 38l-6 6M20 28l4 4M26 22l4 4"/></svg></div>PROLO/ PRP/STEM<br>CELL INJECTIONS</div>
  <div class="abs service" style="left:476px;top:1778px"><div class="ic"><svg width="52" height="52" viewBox="0 0 52 52" fill="none" stroke="#fff" stroke-width="3"><circle cx="26" cy="26" r="5"/><circle cx="13" cy="14" r="4"/><circle cx="39" cy="14" r="4"/><circle cx="26" cy="42" r="4"/><path d="M16 17l6 6M36 17l-6 6M26 31v7"/></svg></div>HYBRID OXYGEN</div>
  <div class="abs service" style="left:700px;top:1752px"><div class="ic"><svg width="52" height="52" viewBox="0 0 52 52" fill="#fff"><rect x="20" y="6" width="12" height="6" rx="2"/><rect x="20" y="15" width="12" height="6" rx="2"/><rect x="21" y="24" width="12" height="6" rx="2"/><rect x="22" y="33" width="12" height="6" rx="2"/><rect x="24" y="42" width="10" height="5" rx="2"/></svg></div>SPINAL<br>DECOMPRESSIONS</div>
  <div class="abs service" style="left:942px;top:1778px"><div class="ic"><svg width="52" height="52" viewBox="0 0 52 52" fill="none" stroke="#fff" stroke-width="3"><circle cx="14" cy="12" r="4"/><path d="M14 18v14h10v10M8 32h16M32 12c3 4-3 8 0 12s-3 8 0 12M40 12c3 4-3 8 0 12s-3 8 0 12"/></svg></div>INFRARED SAUNA</div>

  <div class="abs t-head">PATIENT TESTIMONIALS</div>

  <div class="abs video" style="left:476px;top:2070px;width:332px"><div class="still" role="img" aria-label="Video still of a patient speaking in an exam room"><svg width="84" height="84" viewBox="0 0 84 84"><circle cx="42" cy="42" r="42" fill="#35a3d6" opacity=".85"/><path d="M34 26l24 16-24 16z" fill="#fff"/></svg></div><div class="name">Dana Whitlock</div></div>
  <div class="abs video" style="left:822px;top:2070px;width:332px"><div class="still" role="img" aria-label="Video still of a patient speaking in the clinic lobby"><svg width="84" height="84" viewBox="0 0 84 84"><circle cx="42" cy="42" r="42" fill="#35a3d6" opacity=".85"/><path d="M34 26l24 16-24 16z" fill="#fff"/></svg></div><div class="name">Carol Meyers</div></div>
  <div class="abs video" style="left:476px;top:2368px;width:332px"><div class="still" role="img" aria-label="Video still of a patient speaking beside an eye chart"><svg width="84" height="84" viewBox="0 0 84 84"><circle cx="42" cy="42" r="42" fill="#35a3d6" opacity=".85"/><path d="M34 26l24 16-24 16z" fill="#fff"/></svg></div><div class="name">Ruth Delaney</div></div>
  <div class="abs video" style="left:822px;top:2368px;width:332px"><div class="still" role="img" aria-label="Video still of a patient speaking in a treatment room"><svg width="84" height="84" viewBox="0 0 84 84"><circle cx="42" cy="42" r="42" fill="#35a3d6" opacity=".85"/><path d="M34 26l24 16-24 16z" fill="#fff"/></svg></div><div class="name">Megan Holloway</div></div>
  <div class="abs video" style="left:476px;top:2666px;width:678px"><div class="still" role="img" aria-label="Video still of a patient speaking in a hallway"><svg width="84" height="84" viewBox="0 0 84 84"><circle cx="42" cy="42" r="42" fill="#35a3d6" opacity=".85"/><path d="M34 26l24 16-24 16z" fill="#fff"/></svg></div><div class="name">Iris Caldwell</div></div>
</div>
</body>
</html>
```